Brochure Design Project for Whole Body Cryotherapy

We need a dynamic and call to action brochure of our new whole body cryotherapy. Focusing on Weight loss, sports performance, health and pain relief management. Complete with testimonials, media, users, and complete design and branding using our brand guidelines.

Target Market(s)

people who are aesthetics and health conscious. Plus people who are in for the latest and most hyped technology available

Industry/Entity Type

Health

Requirements
Must have
• important media and users . researching is important. we are in asia and singapore. its the first ever whole body cryotherapy. therefore is a big launch and totally brand new device. We need to creat a very very big hype.

```html
<!DOCTYPE html>
<html lang="en">
<head>
<meta charset="utf-8">
<title>Polar Point – Whole Body Cryotherapy Brochure</title>
<link rel="stylesheet" href="https://fonts.googleapis.com/css2?family=Source+Sans+3:wght@300;400;600;700&display=swap">
<style>
:root{
  --navy:#1d3462;
  --navy-deep:#14254a;
  --blue:#2b9fdb;
  --sky:#55b6e8;
  --ink:#3a3f4a;
  --grey:#6d7480;
  --paper:#ffffff;
  --stage:#ffffff;
  --tile-line:#e3e6ea;
}
*{box-sizing:border-box;margin:0;padding:0}
html,body{width:839px;height:1200px;overflow:hidden;background:var(--stage)}
body{font-family:"Source Sans 3",Arial,sans-serif;color:var(--ink)}
.sheet{position:relative;width:800px;height:1141px;transform:scale(1.04875);transform-origin:0 0}
.abs{position:absolute}
.section-label{position:absolute;font-size:11px;font-weight:600;letter-spacing:.3px;color:#222}
.spread{position:absolute;box-shadow:0 1px 6px rgba(0,0,0,.35);overflow:hidden;background:var(--paper)}
.outer{left:32px;top:36px;width:743px;height:526px}
.inner{left:32px;top:595px;width:743px;height:523px}
.panel{position:absolute;top:0;height:100%;overflow:hidden}

/* flap */
.flap{left:0;width:247px;background:var(--navy)}
.flap .photo{position:absolute;inset:0;background:linear-gradient(160deg,#3a4458 0%,#9aa2ad 45%,#2c2f36 75%,#0c0d10 100%)}
.flap svg{position:absolute;inset:0}
.flap-copy{position:absolute;left:33px;top:58px;width:172px;font-size:10.5px;line-height:1.2;color:#c9d3e6}
.flap-copy p+p{margin-top:10px}
.flap-copy strong{color:var(--sky);font-weight:700}
.flap-title{position:absolute;left:38px;top:452px;color:#fff;font-size:16px;font-weight:300;line-height:1.25}
.flap-title b{font-weight:700;display:block}

/* back */
.back{left:247px;width:248px;background:var(--paper)}
.media-grid{position:absolute;left:15px;top:53px;display:grid;grid-template-columns:repeat(3,65px);grid-auto-rows:62px;gap:5px 7px}
.media-tile{background:#fff;border-radius:3px;box-shadow:0 0 4px rgba(0,0,0,.18);display:flex;align-items:center;justify-content:center}
.media-badge{width:44px;height:22px;border-radius:3px;background:#c9ced6}
.media-badge.round{width:28px;height:28px;border-radius:50%}
.back-rule{position:absolute;left:0;right:0;top:390px;border-top:1px solid var(--tile-line)}
.brand{display:flex;align-items:center;gap:6px}
.brand-dot{border-radius:50%;background:var(--blue)}
.brand-name{font-weight:400;letter-spacing:.5px}
.back .brand{position:absolute;left:58px;top:410px}
.back .brand-dot{width:28px;height:28px}
.back .brand-name{font-size:10px;color:var(--grey)}
.contact{position:absolute;left:21px;top:461px;width:150px;font-size:8.5px;line-height:1.2;color:var(--grey)}
.contact h3{font-size:8.5px;font-weight:700;color:var(--navy)}
.social{position:absolute;left:164px;top:479px;display:flex;gap:5px}
.social span{width:17px;height:17px;background:var(--navy)}

/* cover */
.cover{left:495px;width:248px;background:#f2f3f4}
.cover .photo{position:absolute;left:0;top:0;width:248px;height:424px;background:linear-gradient(170deg,#5a5d62 0%,#9a9ea4 30%,#d7d9dc 60%,#f4f5f6 100%)}
.cover svg{position:absolute;left:0;top:0}
.cover-head{position:absolute;left:0;width:248px;text-align:center;color:var(--navy)}
.cover-head .l1{font-size:30px;font-weight:400;line-height:1}
.cover-head .l2{font-size:30px;font-weight:700;line-height:1.05}
.cover-head .l3{font-size:13px;margin-top:14px}
.cover-head .l4{font-size:13px;font-weight:700}
.cover-band{position:absolute;left:0;bottom:0;width:248px;height:102px;background:var(--navy)}
.cover-band .brand{position:absolute;left:67px;top:25px}
.cover-band .brand-dot{width:40px;height:40px}
.cover-band .brand-name{font-size:11px;color:#fff}

/* inside */
.inner-photo{position:absolute;left:0;top:0;width:743px;height:205px;background:linear-gradient(90deg,#0e2f5c 0%,#1e5b95 22%,#2a2d33 38%,#8d9096 55%,#2a2b2e 70%)}
.inner svg.shapes{position:absolute;left:0;top:0}
.portrait{position:absolute;left:592px;top:82px;width:150px;height:130px;background:linear-gradient(180deg,#8b96a6,#cfd6df)}
.quote{position:absolute;left:505px;top:22px;color:var(--navy);font-weight:700;line-height:1}
.quote .q1{font-size:15px}
.quote .q2{font-size:15px}
.quote .q3{font-size:30px}
.treat-title{position:absolute;left:26px;top:52px;color:#fff;font-size:15px;font-weight:300;line-height:1.2}
.treat-title b{display:block;font-size:18px;font-weight:700}
.treat-copy{position:absolute;left:26px;top:115px;width:218px;color:#fff;font-size:8.6px;font-weight:700;line-height:1.18}

.col{position:absolute;top:205px;height:318px}
.col-beauty{left:0;width:247px;background:#fff}
.col-health{left:247px;width:248px;background:var(--navy);top:200px;height:323px}
.col-sports{left:495px;width:248px;background:#fff}
.beauty-band{position:absolute;left:0;top:0;width:247px;height:38px;background:var(--sky)}
.col h2{position:absolute;font-size:15px;font-weight:400;line-height:1}
.col h2 b{font-weight:700}
.col-beauty h2{left:26px;top:13px;color:#fff}
.col-health h2{left:25px;top:22px;color:var(--sky)}
.col-sports h2{left:24px;top:18px;color:var(--blue)}
.copy{position:absolute;width:210px;font-size:9px;line-height:1.2}
.col-beauty .copy{left:26px;top:45px;color:#8c929b}
.col-health .copy{left:25px;top:48px;color:#d7dfec}
.col-sports .copy{left:24px;top:44px;color:var(--grey)}
.copy h4{font-size:9px;font-weight:700;margin-top:10px}
.col-beauty h4,.col-sports h4{color:var(--navy)}
.col-health h4{color:#fff}
.copy ul{list-style:none}
.copy li::before{content:"•";color:var(--blue);margin-right:3px}
.col-health li::before{color:#fff}
.col-sports .brand{position:absolute;left:106px;top:266px}
.col-sports .brand-dot{width:34px;height:34px}
.col-sports .brand-name{font-size:10px;color:var(--grey)}
</style>
</head>
<body>
<div class="sheet">
  <div class="section-label" style="left:38px;top:12px">FLAP</div>
  <div class="section-label" style="left:316px;top:12px">BACK</div>
  <div class="section-label" style="left:531px;top:12px">COVER</div>
  <div class="section-label" style="left:32px;top:571px">INSIDE</div>

  <!-- outer face -->
  <div class="spread outer">
    <section class="panel flap">
      <div class="photo" role="img" aria-label="Black and white photo of an astronaut in a space suit"></div>
      <svg width="247" height="526" viewBox="0 0 247 526" aria-hidden="true">
        <polygon points="0,0 247,0 247,210 128,430 40,150 0,120" fill="#1d3462" opacity=".96"/>
        <polygon points="150,0 247,0 247,130" fill="#2a4373" opacity=".7"/>
      </svg>
      <div class="flap-copy">
        <p><strong>Whole Body Cryotherapy</strong> (WBC) is a hypothermic application designed to reduce muscoloskeletal pain and inflammation.</p>
        <p>WBC stimulates the nervous system through skin receptors, causing dramatic peripheral vasoconstriction. This induces adaptive changes correlating with effects of analgesia, reduction of inflammation, and increases in serum markers of tissue repair.</p>
      </div>
      <h2 class="flap-title">ABOUT WHOLE BODY<b>CRYOTHERAPY</b></h2>
    </section>

    <section class="panel back">
      <div class="media-grid" aria-label="As featured in media">
        <div class="media-tile"><span class="media-badge"></span></div>
        <div class="media-tile"><span class="media-badge"></span></div>
        <div class="media-tile"><span class="media-badge"></span></div>
        <div class="media-tile"><span class="media-badge round"></span></div>
        <div class="media-tile"><span class="media-badge"></span></div>
        <div class="media-tile"><span class="media-badge"></span></div>
        <div class="media-tile"><span class="media-badge round"></span></div>
        <div class="media-tile"><span class="media-badge"></span></div>
        <div class="media-tile"><span class="media-badge"></span></div>
        <div class="media-tile"><span class="media-badge"></span></div>
        <div class="media-tile"><span class="media-badge"></span></div>
        <div class="media-tile"><span class="media-badge round"></span></div>
        <div class="media-tile"><span class="media-badge"></span></div>
        <div class="media-tile"><span class="media-badge round"></span></div>
        <div class="media-tile"><span class="media-badge"></span></div>
      </div>
      <div class="back-rule"></div>
      <div class="brand"><span class="brand-dot"></span><span class="brand-name">POLAR POINT</span></div>
      <div class="contact">
        <h3>CONTACT DETAILS</h3>
        <p>sertu mod cre consuloc, telinam di pos et que accum deatum nicienti tamdit.</p>
      </div>
      <div class="social" aria-label="Social links"><span></span><span></span><span></span></div>
    </section>

    <section class="panel cover">
      <div class="photo" role="img" aria-label="Black and white close-up of a swimmer in cap and goggles"></div>
      <svg width="248" height="424" viewBox="0 0 248 424" aria-hidden="true">
        <polygon points="150,0 248,0 248,50 145,170" fill="#2b9fdb"/>
        <polygon points="0,0 60,0 0,40" fill="#2b9fdb" opacity=".85"/>
      </svg>
      <div class="cover-head" style="top:262px">
        <div class="l1">Better by</div>
        <div class="l2">cold cure</div>
        <div class="l3">ASIAN 1ST</div>
        <div class="l4">WHOLE BODY CRYOTHERAPY</div>
      </div>
      <div class="cover-band">
        <div class="brand"><span class="brand-dot"></span><span class="brand-name">POLAR POINT</span></div>
      </div>
    </section>
  </div>

  <!-- inside -->
  <div class="spread inner">
    <div class="inner-photo" role="img" aria-label="Black and white photo of two athletes gripping hands, with a blue-tinted shoulder at left"></div>
    <svg class="shapes" width="743" height="230" viewBox="0 0 743 230" aria-hidden="true">
      <path d="M495,0 L743,0 L743,225 L495,225 Z" fill="#ffffff"/>
      <polygon points="470,225 743,0 743,12 500,225" fill="#2b9fdb"/>
      <polygon points="495,0 743,0 455,225" fill="#55b6e8"/>
      <path d="M247,0 C320,10 420,-5 495,0 L470,20 C400,10 320,20 247,8 Z" fill="#1d3462" opacity=".85"/>
    </svg>
    <div class="portrait" role="img" aria-label="Photo of a man in a blue shirt"></div>
    <div class="quote"><div class="q1">“GET THE</div><div class="q2">AGENT FROST</div><div class="q3">BODY”</div></div>
    <h2 class="treat-title">WHOLE BODY CRYOTHERAPY<b>TREATMENT</b></h2>
    <p class="treat-copy">Whole Body Cryotherapy treatments are administered individually via a CryoSauna. The cryosauna uses gasiform nitrogen to rapidly lower the skin's top layer to 32°F while cabin temperature drops to a range of (minus) -220°F to -274°F. During the two to three minutes of extreme cold, the brain stimulates the body's organ regulatory functions resulting in energy increase, cell rejuvenation, immune system boost, and overall system self-healing.</p>

    <section class="col col-beauty">
      <div class="beauty-band"></div>
      <h2>Beauty &amp; <b>Spa</b></h2>
      <div class="copy">
        <p>Skincare, Health and Medical Spas in the U.S. are adopting the cryotherapy treatments used for several years in Europe. Whole Body Cryotherapy provides Spas with a holistic treatment that compliments their current menu of services. WBC stimulates collagen production, resulting in anti-aging skin rejuvenation and cellulite reduction. Also, a surge in metabolism consumes 400 to 800 calories, aiding in weight loss.</p>
        <h4>Reported Benefits:</h4>
        <ul>
          <li>Cellulite Reduction</li><li>Tighter and Healthier Skin</li><li>Stronger and Fuller Hair &amp; Nails</li><li>Fewer Skin Blemishes</li><li>Increased Metabolism &amp; Caloric Burn</li><li>Increased Libido</li><li>Increased Collagen Production</li><li>Quicker Surgical Recovery</li>
        </ul>
      </div>
    </section>

    <section class="col col-health">
      <h2>Health &amp; <b>Wellness</b></h2>
      <div class="copy">
        <p>Wellness Centers, Chiropractors, Physical Therapists and Acupuncturists are leading the introduction of Whole Body Cryotherapy to the U.S. population. WBC is an ideal treatment because it is Whole Body, Holistic and Non-Invasive. Clinical studies on WBC have shown immediate benefits to soft tissue, internal organs, the nervous system and energy meridians.</p>
        <h4>Treated Disorders:</h4>
        <ul>
          <li>Fibromyalgia – Chronic Fatigue Syndrome</li><li>Osteoarthritis – Rheumatoid Arthritis</li><li>Osteoporosis – Multiple Sclerosis</li><li>Phantom Pain – Chronic Pain Syndrome</li><li>Ankylosing Sponylitis – Inflammation of the Spine</li><li>Muscle Pain &amp; Inflammation</li><li>Depression &amp; Mood Disorders</li><li>Immune System Improvement</li><li>Delayed Onset Muscle Soreness</li><li>Central Nervous System Disease</li><li>Degenerative Disease of Joints &amp; Spine</li><li>Inflammation of Tendons, Bursa, Joint Capsules</li>
        </ul>
      </div>
    </section>

    <section class="col col-sports">
      <h2>Sports &amp; <b>Fitness</b></h2>
      <div class="copy">
        <p>Athletes have been a driving force behind the growth of whole-body cryotherapy. Game-time or race success is dependent upon their body's ability to train, recover and perform. WBC provides the most effective and convenient treatment that gives these athletes a competitive advantage.</p>
        <h4>Reported Benefits:</h4>
        <ul>
          <li>Cellulite Reduction</li><li>Tighter and Healthier Skin</li><li>Stronger and Fuller Hair &amp; Nails</li><li>Fewer Skin Blemishes</li><li>Increased Metabolism &amp; Caloric Burn</li><li>Increased Libido</li><li>Increased Collagen Production</li><li>Quicker Surgical Recovery</li><li>Treatment of Psoriasis and Dermatitis</li><li>Boosts Lymph Draining and Blood Circulation</li><li>Activates Natural Biological Regeneration</li>
        </ul>
      </div>
      <div class="brand"><span class="brand-dot"></span><span class="brand-name">POLAR POINT</span></div>
    </section>
  </div>
</div>
</body>
</html>
```